Business school needs a web design

Who We are:
Qelvano is a small business school that offers programs in Project Management. The school is based in West Africa and welcomes students from the whole area. Our aim is to become one of the reference business schools in Africa.

Project Brief:
The site will include all informations relevant for different types of visitors that we have: actual and future students, companies, mass media, future employees, ect. It will present information about subscription, list of programs, presentation of the school and its team,etc.

What We want:
This competition is for Design only no coding! We need design for two pages.
We did some wireframing for the home page and the list of programs page. We made them just to show how we imagine the website would look like. But we encourage creative designs, so you don't have to stick to the wireframe models.

Sites We like:
http://www.larchmontgate.example/
http://www.pelvarin.example/fr/etudes.html
http://www.qwd.example/mba/Pages/default.aspx

Color schemes
The logo of the school is red and black. So the color scheme of the website should match that. For the rest, it is opened to your imagination.
Updates

The payment for the project is now garanteed. Good luck to you all !

Target Market(s)

The target market is diversified because we have students of different ages, also company representatives or employees that might visit the website for recruitment purposes. But the majority of our audience should be aged between 20 - 30 years.

Industry/Entity Type

Small Business

Requirements
Must have
• The design must include two pages: a home page and another interior page : might be the list of programs or any other page relevant to the domain. The Home page must include a slide show at the beginning.
The background page must be white.
Nice to have
• The use of flat design for this project is preferred.
The use of Twitter bootstrap as a base for the design is an asset.

```html
<!DOCTYPE html>
<html lang="en">
<head>
<meta charset="utf-8">
<title>Qelvano Business School</title>
<link rel="stylesheet" href="https://fonts.googleapis.com/css2?family=Open+Sans:wght@400;600;700&family=Arimo:wght@400;700&display=swap">
<style>
:root{
  --red:#c4151c;
  --ink:#2c2c2c;
  --text:#5c5c5c;
  --muted:#8a8a8a;
  --dark:#1f1f1f;
  --footer:#575757;
  --footer-deep:#3e3e3e;
  --white:#ffffff;
}
*{box-sizing:border-box;margin:0;padding:0}
html,body{width:1200px;height:2609px;overflow:hidden;background:var(--white)}
body{position:relative;font-family:"Arimo",Arial,sans-serif;color:var(--text)}
.abs{position:absolute}

/* header */
.site-header{left:0;top:0;width:1200px;height:113px;background:var(--white);box-shadow:0 2px 6px rgba(0,0,0,.15);z-index:2}
.brand{left:104px;top:30px;display:flex;align-items:center;gap:10px}
.brand-mark{width:20px;height:20px;background:var(--red)}
.brand-name{font-family:"Open Sans",sans-serif;font-weight:700;font-size:26px;color:var(--dark)}
.util-nav{right:101px;top:10px;font-size:11px;color:var(--muted)}
.util-nav span{margin:0 7px}
.search{left:880px;top:43px;display:flex}
.search-field{width:162px;height:23px;background:#ececec}
.search-btn{width:55px;height:23px;background:#3a3a3a;color:#fff;font-size:12px;font-weight:700;text-align:center;line-height:23px}
.main-nav{right:101px;top:80px;display:flex;gap:40px;font-family:"Open Sans",sans-serif;font-size:13.5px;font-weight:600;color:var(--ink)}
.main-nav .active{background:var(--red);color:#fff;padding:0 9px;margin-right:-8px}

/* hero */
.hero{left:0;top:113px;width:1200px;height:510px;background:linear-gradient(110deg,#c79a6b 0%,#b07a4d 30%,#8c98a8 60%,#dfe4ea 100%)}
.hero-title{left:103px;top:223px;width:250px;height:67px;background:rgba(40,40,40,.85);color:#fff;font-family:"Open Sans",sans-serif;font-weight:600;font-size:17px;line-height:25px;padding:8px 14px}
.hero-title em{font-style:normal;color:var(--red)}
.hero-caption{left:103px;top:311px;width:450px;height:56px;background:rgba(40,40,40,.85);color:#eee;font-size:12px;line-height:18px;padding:10px 8px}
.hero-arrow{left:553px;top:311px;width:32px;height:56px}

/* features */
.feature{top:671px;width:270px}
.feature h3{font-family:"Open Sans",sans-serif;font-size:16px;font-weight:700;color:var(--ink);display:flex;align-items:center;gap:10px;white-space:nowrap}
.feature p{margin-top:38px;font-size:12px;line-height:22px;color:var(--text)}

.divider{left:260px;width:766px;height:12px;background:radial-gradient(ellipse at top,rgba(0,0,0,.12),rgba(0,0,0,0) 70%)}

/* tabs */
.tabs{left:122px;top:976px;display:flex;gap:18px;font-family:"Open Sans",sans-serif;font-size:12px;font-weight:600}
.tab{height:30px;line-height:30px;padding:0 18px}
.tab.plain{color:var(--red);padding:0 12px}
.tab.current{border:1px solid #ccc;border-bottom:none;background:#fff;color:var(--ink);padding:0 24px}
.tab.dark{background:#3a3a3a;color:#fff;width:94px;text-align:center}
.tab-rule{left:122px;top:1005px;width:450px;height:1px;background:#ccc}
.tab-body{left:122px;top:1024px;width:440px;font-size:12px;line-height:22px}
.tab-body ul{margin:14px 0 0 36px}
.tab-body li{line-height:22px;white-space:nowrap}

.photo-ring{border-radius:50%;background:#ececec}
.photo{border-radius:50%;background:radial-gradient(circle at 50% 35%,#6f8f5a 0%,#3a3f3a 45%,#141414 100%)}

/* blog */
.section-title{font-family:"Open Sans",sans-serif;font-size:21px;font-weight:600;color:var(--ink)}
.section-sub{font-size:12px;color:var(--ink)}
.post{width:460px}
.post-thumb{width:83px;height:83px;background:linear-gradient(160deg,#8aa0b8,#4f5a6a 60%,#2d2f36)}
.post-body{left:96px;top:-4px;width:380px}
.post-title{font-family:"Open Sans",sans-serif;font-size:16px;font-weight:600;color:var(--red);white-space:nowrap}
.post-meta{margin-top:4px;font-size:10px;font-weight:700;color:var(--muted);letter-spacing:.3px}
.post-meta b{color:#555;margin-left:8px}
.post-text{margin-top:6px;font-size:12.5px;line-height:23px;color:var(--text)}
.post-more{margin-top:8px;font-size:9.5px;font-weight:700;color:#555;letter-spacing:.3px}

/* partners */
.partner{width:190px;height:44px;border-radius:6px;background:#dcdcdc}

/* footer */
.footer-band{left:0;top:2337px;width:1200px;height:37px;background:var(--dark);color:#fff;font-size:13px;line-height:37px;padding-left:108px}
.footer-main{left:0;top:2374px;width:1200px;height:214px;background:var(--footer)}
.footer-col{top:2406px;color:#eee;font-size:11.5px;line-height:18px}
.footer-col h4{font-family:"Open Sans",sans-serif;font-size:13.5px;font-weight:700;color:#fff;margin-bottom:9px}
.footer-col li{list-style:none;line-height:22px;font-size:12px}
.news-panel{left:840px;top:2337px;width:221px;height:251px;background:var(--footer-deep)}
.social{left:840px;top:2337px;width:221px;height:37px;background:#2a2a2a;display:flex;align-items:center;gap:22px;padding-left:10px}
.social i{display:block;width:12px;height:12px;background:#fff;border-radius:2px}
.news-text{left:851px;top:2386px;width:200px;color:#eee;font-size:10.5px;line-height:15px}
.field{left:851px;width:180px;height:24px;border:1px solid #555;background:#333;color:#eee;font-size:11px;line-height:22px;padding-left:6px}
.submit{left:960px;top:2532px;width:72px;height:22px;background:var(--red);color:#fff;font-size:10px;font-weight:700;text-align:center;line-height:22px}
.copyright{left:0;top:2588px;width:1200px;height:21px;background:var(--dark);color:#ddd;font-size:10px;line-height:21px;text-align:center}
</style>
</head>
<body>

<header class="site-header abs">
  <div class="brand abs"><span class="brand-mark"></span><span class="brand-name">Qelvano</span></div>
  <div class="util-nav abs">Services<span>|</span>Work Examples<span>|</span>Your Team<span>|</span>OurBlog</div>
  <div class="search abs"><div class="search-field"></div><div class="search-btn">Search</div></div>
  <nav class="main-nav abs"><span class="active">Home</span><span>Actual &amp; Future Students</span><span>Companies</span><span>Mass Media</span><span>Future Employees</span></nav>
</header>

<section class="hero abs" role="img" aria-label="Slideshow photo of students taking notes with pens on papers at a desk"></section>
<div class="hero-title abs"><em>Qelvano</em> Program of<br>Project Managment 2014</div>
<div class="hero-caption abs">The school is based in West Africa and welcomes students from the whole area. Our aim is to become one of the reference business schools in Africa.</div>
<svg class="hero-arrow abs" viewBox="0 0 32 56"><polygon points="0,0 32,0 24,56 0,56" fill="#c4151c"/><polyline points="12,22 18,28 12,34" fill="none" stroke="#fff" stroke-width="2.5"/></svg>

<div class="feature abs" style="left:151px">
  <h3><svg width="22" height="20" viewBox="0 0 22 20"><polyline points="2,10 8,16 20,3" fill="none" stroke="#3a3a3a" stroke-width="4"/></svg>Original and excellent designs.</h3>
  <p>Our themes are handcrafted in-house by our designers with attention to detail and pixel perfection. We are always excited to be creating new and out-of-the-box website designs.</p>
</div>
<div class="feature abs" style="left:466px">
  <h3><svg width="22" height="22" viewBox="0 0 22 22"><circle cx="11" cy="11" r="7" fill="none" stroke="#3a3a3a" stroke-width="5" stroke-dasharray="3 2.5"/><circle cx="11" cy="11" r="5" fill="none" stroke="#3a3a3a" stroke-width="3"/></svg>We make it totally simple.</h3>
  <p>Inventing and writing code are our passions - so they don't have to be yours! We love writing code and, for us, there's nothing is quite as fulfilling as making something that is simple and just works.</p>
</div>
<div class="feature abs" style="left:783px">
  <h3><svg width="24" height="20" viewBox="0 0 24 20"><circle cx="9" cy="5" r="4.5" fill="#3a3a3a"/><path d="M1 20c0-7 4-9 8-9s8 2 8 9z" fill="#3a3a3a"/><circle cx="17" cy="6" r="3.5" fill="#3a3a3a"/><path d="M14 12c5-1 9 1 9 8h-5z" fill="#3a3a3a"/></svg>Support you can count on.</h3>
  <p>We give the kind of support we would like to get: fast, helpful, and efficient. And while we won't put together your website for you, we will always be there to guide you in the right direction.</p>
</div>

<div class="divider abs" style="top:908px"></div>

<div class="tabs abs">
  <div class="tab plain">Features</div>
  <div class="tab current">Nouvelles</div>
  <div class="tab dark">Projects</div>
  <div class="tab dark">Supports</div>
</div>
<div class="tab-rule abs"></div>
<div class="tab-body abs">
  <p>Customize things like your logo, background image, and color. Our themes are crafted with you, the user, in mind to make the entire process simple and easy. You will quickly have a very custom-looking website that you can show to the world.</p>
  <ul>
    <li>Upload your own logo</li>
    <li>Change your background colors or images</li>
    <li>Use your own images and videos for a completely customized experience</li>
    <li>Create your own content and easily plug it into great design</li>
  </ul>
</div>
<div class="photo-ring abs" style="left:720px;top:948px;width:358px;height:358px"></div>
<div class="photo abs" role="img" aria-label="Graduates in caps and gowns celebrating in front of a campus building" style="left:734px;top:962px;width:330px;height:330px"></div>
<div class="photo-ring abs" style="left:622px;top:1118px;width:200px;height:200px"></div>
<div class="photo abs" role="img" aria-label="Graduates cheering at a ceremony" style="left:636px;top:1132px;width:172px;height:172px;background:radial-gradient(circle at 50% 40%,#5a4a40,#1c1c1c 80%)"></div>

<div class="divider abs" style="top:1405px"></div>

<div class="abs" style="left:130px;top:1454px">
  <div class="section-title">News From Our Blog</div>
  <div class="section-sub">Latest news and blogs</div>
</div>

<div class="post abs" style="left:130px;top:1534px">
  <div class="post-thumb" role="img" aria-label="Group of students in uniforms"></div>
  <div class="post-body abs">
    <div class="post-title">The standard Lorem Ipsum passage, used since</div>
    <div class="post-meta">FEBRUARY, 15 2013 <b>5 COMMENTS</b></div>
    <div class="post-text">Last night I was browsing a few different sites that run the Quick Shelf Downloads plugin to check how...</div>
    <div class="post-more">CONTINUE READING &rarr;</div>
  </div>
</div>
<div class="post abs" style="left:617px;top:1534px">
  <div class="post-thumb" role="img" aria-label="Students at a seminar" style="background:linear-gradient(160deg,#c9a06a,#6b4b30 60%,#2d2520)"></div>
  <div class="post-body abs">
    <div class="post-title">De Finibus Bonorum et Malorum", written by</div>
    <div class="post-meta">FEBRUARY, 13 2013 <b>5 COMMENTS</b></div>
    <div class="post-text">Over the years of developing themes we have learnt quite a lot in terms of how to best develop...</div>
    <div class="post-more">CONTINUE READING &rarr;</div>
  </div>
</div>
<div class="post abs" style="left:130px;top:1677px">
  <div class="post-thumb" role="img" aria-label="Graduation crowd outside a building" style="background:linear-gradient(160deg,#b9bcc2,#6a6f78 60%,#3a3c42)"></div>
  <div class="post-body abs">
    <div class="post-title">Lorem Ipsum passage, used since the 1500s</div>
    <div class="post-meta">JANUARY, 31 2013 <b>4 COMMENTS</b></div>
    <div class="post-text">This year one of our top priorities is to greatly improve our customer support and we want to be accountable...</div>
    <div class="post-more">CONTINUE READING &rarr;</div>
  </div>
</div>
<div class="post abs" style="left:617px;top:1677px">
  <div class="post-thumb" role="img" aria-label="Graduates gathered in a hall" style="background:linear-gradient(160deg,#8c8fa3,#4a4660 60%,#24222e)"></div>
  <div class="post-body abs">
    <div class="post-title">Translation by H. Rowden</div>
    <div class="post-meta">DECEMBER, 18 2012 <b>74 COMMENTS</b></div>
    <div class="post-text">Here at Fernleaf Themes we are getting in the festive mood and to celebrate we want to share Christmas joy..</div>
    <div class="post-more">CONTINUE READING &rarr;</div>
  </div>
</div>

<div class="divider abs" style="top:1887px"></div>

<div class="section-title abs" style="left:130px;top:1922px">Partnership &amp; Affiliations</div>
<div class="partner abs" style="left:183px;top:1999px"></div>
<div class="partner abs" style="left:496px;top:1999px"></div>
<div class="partner abs" style="left:797px;top:1999px"></div>
<div class="partner abs" style="left:183px;top:2094px"></div>
<div class="partner abs" style="left:496px;top:2094px"></div>
<div class="partner abs" style="left:797px;top:2094px"></div>

<div class="divider abs" style="top:2261px"></div>

<div class="footer-band abs">Qelvano is a small business school that offers programs in Project Management...</div>
<div class="footer-main abs"></div>
<div class="footer-col abs" style="left:110px;width:264px">
  <h4>About Us</h4>
  <p>Users will feel the speed.<br>Interchange now enables HTML partials for device specific content. Smoother animations and transitions happen with hardware accel-eration. The default styles are all updated.</p>
</div>
<div class="footer-col abs" style="left:450px">
  <h4>Services</h4>
  <ul><li>Resources</li><li>Management</li><li>Addmissions</li><li>Scholarships</li><li>Events</li></ul>
</div>
<div class="footer-col abs" style="left:649px">
  <h4>Managments</h4>
  <ul><li>Graduatons</li><li>Project Manager</li><li>Establishments</li><li>Others</li></ul>
</div>
<div class="news-panel abs"></div>
<div class="social abs">
  <svg width="14" height="11" viewBox="0 0 14 11"><rect x="0.5" y="0.5" width="13" height="10" fill="#fff"/><polyline points="0.5,0.5 7,6 13.5,0.5" fill="none" stroke="#2a2a2a"/></svg>
  <i></i><i></i><i></i><i></i><i></i>
</div>
<div class="news-text abs">Get the latest Larchmont research on topics such as entrepreneurship, marketing, decision research, corporate governance and labor economics. Sign-up to have <em>Ledger Notes</em> delivered to you.</div>
<div class="field abs" style="top:2470px">first name</div>
<div class="field abs" style="top:2500px">last name</div>
<div class="field abs" style="top:2531px;width:100px;border:none;background:none">email address</div>
<div class="submit abs">SUBMIT &raquo;</div>
<div class="copyright abs">Copyright c 2014.Business School.All Right Reserved</div>

</body>
</html>
```